Re-design of website

I have an existing website that I would like to improve. The functionality will remain the same but the overall look will need to be changed. I have some ideas of what i would like included and am also in need of someone else to input their own creative ideas. I am on a tight deadline to get these improvements made as I have many people being directed to the site via our advertising campaigns that are in full swing late next week. Thanks
Target Market(s)
The website provides a virtual space for families to learn more about our learning program which we operate out of Dubai and will soon spread to the other Emirates. The families are generally between 25-50 year old parents with children up to the age of 6. They are local Emirati's as well as expats.

```html
<!DOCTYPE html>
<html lang="en">
<head>
<meta charset="utf-8">
<title>Bright Sprouts – Accelerated Learning Centre</title>
<link href="https://fonts.googleapis.com/css2?family=Play:wght@400;700&family=Comic+Neue:wght@700&family=Arimo:wght@400&display=swap" rel="stylesheet">
<style>
:root{
  --orange:#f2963e;
  --orange-deep:#fb6c37;
  --grey-panel:#999999;
  --steel:#5a8ea9;
  --ink:#3a3a3a;
  --muted:#8a8a8a;
  --stripe-a:#f4f4f4;
  --stripe-b:#ebebeb;
  --white:#ffffff;
  --fb:#4f6da8;
  --tw:#1fb8f0;
}
*{box-sizing:border-box;margin:0;padding:0}
html,body{width:950px;height:1200px;overflow:hidden}
body{position:relative;background:var(--white);font-family:"Arimo",Arial,sans-serif;color:var(--ink)}
.abs{position:absolute}
.stripes{left:0;top:0;width:950px;height:458px;
  background:repeating-linear-gradient(90deg,var(--stripe-a) 0 6px,var(--stripe-b) 6px 9px)}
.fade{left:0;top:458px;width:950px;height:150px;background:linear-gradient(#ececec,#fff)}
.band-top{left:0;top:0;width:950px;height:20px;background:var(--steel)}
.band-bottom{left:0;top:1170px;width:950px;height:30px;background:var(--orange)}
.brand{left:60px;top:95px;display:flex;align-items:center;gap:10px}
.brand-dot{width:26px;height:26px;border-radius:50%;background:var(--steel)}
.brand-name{font-family:"Play",sans-serif;font-weight:700;font-size:24px;color:var(--steel)}
.hero-kids{left:337px;top:43px;width:250px;height:205px;border-radius:40px;
  background:radial-gradient(circle at 50% 45%,#f6d7a6,#e9eef2 70%)}
.register{left:595px;top:14px;width:110px;height:110px;border-radius:50%;background:var(--orange);
  color:#fff;font-family:"Play",sans-serif;font-weight:700;font-size:18px;line-height:19px;
  display:flex;align-items:center;justify-content:center;text-align:center}
.go{left:692px;top:37px;width:64px;height:64px;border-radius:50%;background:#fff;border:2px solid var(--orange);
  font-family:"Play",sans-serif;font-weight:700;font-size:17px;color:#666;text-align:center;padding-top:8px}
.go svg{display:block;margin:2px auto 0}
.hotline{left:680px;top:123px;width:200px;text-align:center;font-family:"Play",sans-serif;font-size:16px;color:#555;line-height:24px}
.hotline .num{color:var(--muted);font-size:17px}
.social{top:181px;width:44px;height:52px}
.nav{left:51px;top:251px;display:flex;gap:5px}
.nav a{height:34px;border:2px solid #e2e2e2;border-radius:17px;background:#fff;font-family:"Play",sans-serif;
  font-weight:700;font-size:14px;color:#8a8a8a;text-decoration:none;display:flex;align-items:center;justify-content:center}
.nav a.active{background:var(--orange);border-color:var(--orange);color:#fff}
.hero{left:51px;top:296px;width:846px;height:345px;border:1px solid #dcdcdc;background:#fff;box-shadow:0 6px 10px rgba(0,0,0,.06)}
.hero-photo{left:12px;top:10px;width:582px;height:308px;border-radius:6px;
  background:
    linear-gradient(180deg,rgba(255,255,255,.85) 0%,rgba(255,255,255,0) 18%,rgba(255,255,255,0) 88%,rgba(255,255,255,.9) 100%),
    linear-gradient(90deg,#f5d36a 0%,#f3b7c6 18%,#f6e27c 32%,#cdbde6 46%,#f0a060 60%,#9fcf86 74%,#e86a5a 88%,#f4f4f4 100%)}
.dots{left:292px;top:324px;display:flex;gap:7px}
.dots i{width:10px;height:10px;border-radius:50%;background:#aaa}
.dots i:first-child{background:#444}
.hero-side{left:594px;top:0;width:251px;height:343px;background:var(--orange)}
.hero-boy{left:40px;top:28px;width:60px;height:125px;border-radius:20px;background:linear-gradient(#e98a3e,#6d94c4)}
.hero-brain{left:108px;top:40px;width:110px;height:110px;border-radius:50%;background:#3b3b3b}
.hero-text{left:12px;top:174px;width:227px;text-align:center;font-family:"Comic Neue",cursive;font-weight:700;
  font-size:21px;line-height:22.7px;color:#fff}
.card{top:687px;width:276px;height:386px;color:#fff}
.card h2{position:absolute;left:20px;top:12px;font-family:"Play",sans-serif;font-weight:400;font-size:23px}
.card .rule{position:absolute;left:16px;top:44px;width:244px;height:1px;background:rgba(255,255,255,.7)}
.card .frame{position:absolute;left:16px;top:59px;width:244px;height:146px;background:#fff;border-radius:5px;padding:8px}
.card .frame div{width:100%;height:100%}
.card p{position:absolute;left:22px;width:238px;font-size:11.2px;line-height:14.6px}
.more{position:absolute;left:191px;top:352px;width:69px;height:22px;background:#fff;color:#333;font-size:11.5px;
  text-decoration:underline;display:flex;align-items:center;justify-content:center}
.company{left:51px;background:var(--grey-panel)}
.program{left:336px;background:var(--orange-deep)}
.media{left:621px;background:var(--orange)}
.player{position:absolute;left:16px;top:60px;width:247px;height:177px;background:#222;overflow:hidden}
.player .scene{position:absolute;left:0;top:18px;width:247px;height:140px;background:linear-gradient(90deg,#5d1f22,#8a4a46 50%,#4a2a30)}
.player .title{position:absolute;left:7px;top:4px;font-size:8px;color:#fff}
.player .bar{position:absolute;left:0;bottom:0;width:247px;height:19px;background:#1a1a1a;font-size:6.5px;color:#ccc;padding:6px 0 0 48px}
.footer-rule{left:24px;top:1086px;width:899px;height:1px;background:#bbb}
.footer-links{left:0;top:1105px;width:950px;text-align:center;font-family:"Play",sans-serif;font-weight:700;font-size:14px;color:#333}
.copy{left:0;top:1128px;width:950px;text-align:center;font-size:10.5px;color:#555}
</style>
</head>
<body>
<div class="abs stripes"></div>
<div class="abs fade"></div>
<div class="abs band-top"></div>

<div class="abs brand"><span class="brand-dot"></span><span class="brand-name">Bright Sprouts</span></div>

<div class="abs hero-kids" role="img" aria-label="Illustration of two cartoon school children walking hand in hand with backpacks"></div>

<div class="abs register">Register<br>your<br>interest<br>today!</div>
<div class="abs go">Go
  <svg width="22" height="20" viewBox="0 0 22 20"><path d="M1 6h11V1l9 9-9 9v-5H1z" fill="#3f79c6"/></svg>
</div>

<div class="abs hotline">Hotline phone number<br><span class="num">+971 555 012 340</span></div>

<svg class="abs social" style="left:734px" viewBox="0 0 44 52" aria-label="Social link"><path d="M0 0h44v52l-22-11L0 52z" fill="var(--fb)"/></svg>
<svg class="abs social" style="left:786px" viewBox="0 0 44 52" aria-label="Social link"><path d="M0 0h44v52l-22-11L0 52z" fill="var(--tw)"/></svg>

<nav class="abs nav">
  <a class="active" style="width:86px">Home</a>
  <a style="width:114px">Our Method</a>
  <a style="width:121px">The Program</a>
  <a style="width:86px">Media</a>
  <a style="width:96px">Locations</a>
  <a style="width:94px">About Us</a>
  <a style="width:103px">Contact Us</a>
  <a style="width:119px">News &amp; Events</a>
</nav>

<section class="abs hero">
  <div class="abs hero-photo" role="img" aria-label="Photo of a row of seven smiling young children in colourful clothes standing against a white wall"></div>
  <div class="abs dots"><i></i><i></i><i></i><i></i></div>
  <div class="abs hero-side">
    <div class="abs hero-boy" role="img" aria-label="Illustration of a boy with a backpack"></div>
    <div class="abs hero-brain" role="img" aria-label="White brain symbol in a dark circle"></div>
    <p class="abs hero-text">The brain develops<br>almost entirely between<br>the age 0 to 6 years old.<br>Let us help your child<br>to be the best they<br>can be!</p>
  </div>
</section>

<section class="abs card company">
  <h2>Our Company</h2><div class="rule"></div>
  <div class="frame"><div role="img" aria-label="Photo of a mother and baby playing with stacking blocks" style="background:linear-gradient(135deg,#c98a55,#f1e4d6 60%,#e6c9a6)"></div></div>
  <p style="top:218px">Bright Sprouts Accelerated Learning Centre is the first a whole brain training program designed to maximise your child's potential during this key period of development.</p>
  <a class="more">more info</a>
</section>

<section class="abs card program">
  <h2>The Program</h2><div class="rule"></div>
  <div class="frame"><div role="img" aria-label="Photo of a toddler playing with an abacus and learning cards" style="background:linear-gradient(135deg,#d9cfc4,#9fb1c8 50%,#e4dad0)"></div></div>
  <p style="top:219px">Our preschool program and accelerated learning activities are for the early learner age group 6 months to 6 years old.<br><br>We currently offer the program in English.<br><br>Our classes are 50 minutes and we request a parent or carer to attend the class with the child.</p>
  <a class="more">more info</a>
</section>

<section class="abs card media">
  <h2>Media</h2><div class="rule"></div>
  <div class="player">
    <div class="scene" role="img" aria-label="Video still of a speaker at a podium with an audience behind"></div>
    <span class="title">Ellen Marsh Talk on Early Childhood Learning</span>
    <svg style="position:absolute;left:104px;top:76px" width="38" height="26" viewBox="0 0 38 26"><rect width="38" height="26" rx="5" fill="rgba(0,0,0,.75)"/><path d="M15 7l10 6-10 6z" fill="#fff"/></svg>
    <div class="bar">00:00 / 15:49</div>
    <svg style="position:absolute;left:12px;bottom:5px" width="30" height="9" viewBox="0 0 30 9"><path d="M0 0l7 4.5L0 9z M16 3h3l3-3v9l-3-3h-3z" fill="#bbb"/></svg>
  </div>
  <p style="top:254px">Governor Ellen Marsh urging citizens to encourage learning at the earliest possible age in a child's life. "Study after study shows that the earlier a child begins learning the better he or she does down the road"</p>
  <a class="more" style="top:354px">more info</a>
</section>

<div class="abs footer-rule"></div>
<div class="abs footer-links">Home | Our Method | The Program | Media | Locations | About Us | Contact Us | News &amp; Events</div>
<div class="abs copy">©2013 Bright Sprouts, All rights reserved.</div>

<div class="abs band-bottom"></div>
</body>
</html>
```